DESIGN A LEAFLET FOR A CANNABIS CLUB!!

We need a leaflet design for a cannabis club based in the United Kingdom, called Silver Brook Cannabis Club

PLEASE, FEEL FREE TO ADD YOUR OWN INFO ETC

Just want attention drawn to the INSTAGRAM/WEBSITE whilst looking semi-professional

LEGALIZE IT (title)

Government officials are denying your right to access legal Cannabis.

Over Thirty-five countries already have legal access in one form or another... What are we waiting for ?

I'd ideally like the leaflet to be A6 size

"INSTAGRAM LOGO": Silverbrookcannabisclub
*MUST SEE*
"FACEBOOK LOGO": Silverbrookcannabisclub
WEB: www.silverbrookcannabisclub.example

Check us out!
*Cannabis Discussion Forum*
*Weed related news*
*Awesome Documentaries*

Industry/Entity Type

Club

Requirements
Must have
• Please use my logo on leaflet somewhere, feel free to re-size it
• Back of leaflet to just have my cannabis logo in large with green and smoky background
Nice to have
• PLEASE, FEEL FREE TO ADD YOUR OWN INFO ETC
• Just want attention drawn to INSTAGRAM/WEBSITE whilst looking semi-professional
Should not have
• Plain, boring, minimal effort

```html
<!DOCTYPE html>
<html lang="en">
<head>
<meta charset="utf-8">
<title>Silver Brook Cannabis Club – Leaflet</title>
<link href="https://fonts.googleapis.com/css2?family=Lato:wght@700;900&family=Oswald:wght@500;600;700&display=swap" rel="stylesheet">
<style>
  :root{
    --backdrop:#7b9a62;
    --header-light:#ffffff;
    --header-dark:#c4c6c5;
    --green-deep:#0f7a2c;
    --green-mid:#2fa043;
    --green-light:#8fd08a;
    --mint:#dcece0;
    --ink:#2f3b2c;
    --brown:#8a5a2e;
    --white:#ffffff;
  }
  *{box-sizing:border-box;margin:0;padding:0}
  html,body{width:1200px;height:803px;overflow:hidden}
  body{background:var(--backdrop);position:relative}
  .leaflet{
    position:absolute;left:338px;top:31px;width:524px;height:740px;
    background:var(--mint);overflow:hidden;
    box-shadow:0 10px 30px rgba(0,0,0,.25);
  }
  .header{
    position:absolute;left:0;top:0;width:100%;height:240px;
    background:linear-gradient(180deg,var(--header-light) 0%,var(--header-dark) 100%);
  }
  .brand{
    position:absolute;left:0;top:90px;width:100%;
    display:flex;align-items:center;justify-content:center;gap:10px;
  }
  .brand-mark{width:24px;height:24px;border-radius:50%;background:var(--green-mid)}
  .brand-name{
    font-family:"Oswald",sans-serif;font-weight:600;font-size:21px;
    color:var(--green-deep);letter-spacing:.4px;
  }
  .photo-strip{
    position:absolute;left:0;top:236px;width:100%;height:160px;
    display:flex;gap:6px;padding:0 6px;
  }
  .photo{flex:1;border:4px solid var(--white);border-bottom:none}
  .photo-buds{background:linear-gradient(135deg,#b9b48a,#7f8b4a 60%,#5d6a33)}
  .photo-smoker{background:linear-gradient(135deg,#3a2f36,#a78a86 55%,#d8d2d0)}
  .photo-plants{background:linear-gradient(135deg,#e6eee2,#6fa35a 60%,#2d6a2a)}
  .swoosh{position:absolute;left:0;width:100%;display:block}
  .swoosh-top{top:170px;height:90px}
  .swoosh-mid{top:340px;height:80px}
  .content{position:absolute;left:40px;top:412px;width:444px}
  .kicker{font-family:"Oswald",sans-serif;font-weight:600;font-size:28px;color:var(--ink);line-height:1.05}
  .headline{font-family:"Oswald",sans-serif;font-weight:500;font-size:62px;color:var(--brown);line-height:1;margin-top:2px}
  .message{font-family:"Oswald",sans-serif;font-weight:700;font-size:15.5px;color:var(--ink);line-height:1.3;margin-top:12px;width:390px}
  .socials{
    position:absolute;left:40px;top:612px;width:420px;height:34px;
    background:var(--white);border-radius:17px;
    display:flex;align-items:center;justify-content:space-around;
    box-shadow:0 1px 3px rgba(0,0,0,.2);
  }
  .social{display:flex;align-items:center;gap:6px;font-family:"Lato",sans-serif;font-weight:700;font-size:11px;color:var(--ink)}
  .social-mark{width:14px;height:14px;background:var(--ink)}
  .footer-band{position:absolute;left:0;bottom:0;width:100%;height:96px}
  .website{
    position:absolute;left:0;bottom:22px;width:100%;text-align:center;
    font-family:"Lato",sans-serif;font-weight:900;font-size:21px;color:var(--white);letter-spacing:.3px;
  }
</style>
</head>
<body>
  <article class="leaflet">
    <header class="header">
      <div class="brand">
        <span class="brand-mark"></span>
        <span class="brand-name">Silver Brook Cannabis Club</span>
      </div>
    </header>

    <div class="photo-strip">
      <div class="photo photo-buds" role="img" aria-label="Close-up photo of dried cannabis buds"></div>
      <div class="photo photo-smoker" role="img" aria-label="Photo of a club member exhaling smoke"></div>
      <div class="photo photo-plants" role="img" aria-label="Photo of cannabis plants growing"></div>
    </div>

    <svg class="swoosh swoosh-top" viewBox="0 0 524 90" preserveAspectRatio="none" aria-hidden="true">
      <path d="M0 60 C160 20 360 12 524 30 L524 66 C360 50 170 58 0 90 Z" fill="var(--green-light)"/>
      <path d="M0 70 C170 32 360 24 524 42 L524 60 C360 46 170 54 0 86 Z" fill="var(--green-deep)"/>
      <path d="M0 78 C170 44 360 36 524 52 L524 58 C360 46 170 54 0 84 Z" fill="var(--white)"/>
    </svg>

    <svg class="swoosh swoosh-mid" viewBox="0 0 524 80" preserveAspectRatio="none" aria-hidden="true">
      <path d="M0 34 C150 70 330 14 524 0 L524 80 L0 80 Z" fill="var(--green-deep)"/>
      <path d="M0 44 C150 78 330 26 524 14 L524 80 L0 80 Z" fill="var(--green-mid)"/>
      <path d="M0 54 C150 84 330 38 524 28 L524 80 L0 80 Z" fill="var(--mint)"/>
    </svg>

    <section class="content">
      <h2 class="kicker">Maintenance</h2>
      <h1 class="headline">Mode is On</h1>
      <p class="message">Government Officials want to deny your right to access Legal Cannabis, over thirty-five countries already have access in one form or another... Why shouldn't you?</p>
    </section>

    <div class="socials">
      <span class="social"><span class="social-mark"></span>Silverbrookcannabisclub</span>
      <span class="social"><span class="social-mark"></span>Silverbrookcannabisclub</span>
    </div>

    <svg class="footer-band" viewBox="0 0 524 96" preserveAspectRatio="none" aria-hidden="true">
      <path d="M0 28 C180 0 360 10 524 0 L524 96 L0 96 Z" fill="var(--green-light)"/>
      <path d="M0 38 C180 12 360 22 524 12 L524 96 L0 96 Z" fill="var(--green-deep)"/>
    </svg>
    <p class="website">www.silverbrookcannabisclub.example</p>
  </article>
</body>
</html>
```